Luggage and travel essentials company needs Letterhead design (including logo)

Brambury luggage is a travel retailer focussed on selling luggage and travel essentials.
We are a company that have a traditional approach to customer service and also embraces the latest technology, especially where it improves the customer experience.
I would like the design to have an airport hint (airport imagery and font preferred), I would also like the colour blue to feature heavily (see attached image for colour hint).
The final design should aim to give the customer confidence that we are dependable and reliable (no script fonts or crazy colours please) but also reflect that we are an innovative and technology focused company.
I would like the letterhead design to include a logo and text.
I am interested in letterhead text containing an embedded logo (much like the 'Z' in Zephyra's logo is also used separately) Note: this is optional.
The text of the letterhead should include the words "Brambury Luggage & Travel Essentials", and should include a space for the company phone number, email address, website address along with the company physical address.
Target Market(s)
Affluent Adults aged 25 years and above - Predominantly female
Industry/Entity Type
Airport

```html
<!DOCTYPE html>
<html lang="en">
<head>
<meta charset="utf-8">
<title>Brambury Luggage &amp; Travel Essentials — Letterhead</title>
<link href="https://fonts.googleapis.com/css2?family=Lato:wght@400;700&display=swap" rel="stylesheet">
<style>
  :root {
    --backdrop: #e3e7e9;
    --paper: #ffffff;
    --brand-blue: #1a96d4;
    --ink: #2f3234;
    --ink-soft: #4a4d50;
    --signature-tone: #eef1f3;
  }
  * { box-sizing: border-box; margin: 0; padding: 0; }
  html, body {
    width: 900px; height: 1200px; overflow: hidden;
    background: var(--backdrop);
    font-family: "Lato", Arial, sans-serif;
    color: var(--ink);
  }
  .letterhead {
    position: absolute; left: 36px; top: 38px;
    width: 824px; height: 1124px;
    background: var(--paper);
    border-radius: 22px;
    box-shadow: 0 2px 8px rgba(0,0,0,0.18);
    overflow: hidden;
  }
  .brand {
    position: absolute; left: 92px; top: 92px;
    display: flex; align-items: center; gap: 10px;
  }
  .brand-dot {
    width: 44px; height: 44px; border-radius: 50%;
    background: var(--brand-blue); flex: none;
  }
  .brand-name {
    font-weight: 700; font-size: 15px; line-height: 17px;
    color: var(--brand-blue);
  }
  .salutation {
    position: absolute; left: 91px; top: 287px;
    font-size: 19px; color: var(--ink);
  }
  .body-copy {
    position: absolute; left: 91px; top: 358px; width: 610px;
    font-size: 13.8px; line-height: 22.3px; color: var(--ink-soft);
    text-align: justify; hyphens: auto; -webkit-hyphens: auto;
  }
  .body-copy p + p { margin-top: 20px; }
  .sender { position: absolute; left: 91px; top: 753px; }
  .sender-name { font-size: 18px; color: var(--ink); }
  .sender-role { font-size: 12px; color: var(--ink-soft); margin-top: 9px; }
  .signature {
    position: absolute; left: 70px; top: 848px;
    width: 166px; height: 74px;
    background: var(--signature-tone); border-radius: 6px;
  }
  .contact {
    position: absolute; left: 88px; top: 1033px;
    font-size: 12px; color: var(--ink-soft);
  }
  .contact-row { display: flex; height: 25px; align-items: center; }
  .contact-item { display: inline-flex; gap: 10px; }
  .contact-item.phone { width: 155px; }
  .contact-item.mail { width: 200px; }
  .contact-label { color: var(--brand-blue); }
</style>
</head>
<body>
  <main class="letterhead">
    <div class="brand">
      <span class="brand-dot"></span>
      <span class="brand-name">Brambury Luggage<br>&amp; Travel Essentials</span>
    </div>

    <p class="salutation">Dear Mr. Smith,</p>

    <div class="body-copy">
      <p>Lorem ipsum dolor sit amet, consectetur adipiscing elit. Donec orci purus, luctus vitae dignissim eu, iaculis sed purus. Vivamus faucibus, ipsum nec aliquet viverra, leo mauris condimentum ligula, sit amet sagittis enim ligula quis arcu. Nam egestas tortor id nisi porttitor mattis. In tortor ante, ultricies in suscipit a, tempus non massa. Vivamus et auctor mi. Fusce vel massa nulla. Phasellus nec eros mauris, et scelerisque orci. Donec malesuada orci vitae nulla accumsan porta a id massa. Quisque accumsan iaculis magna sit amet fringilla. Maecenas consequat, magna eget tincidunt semper, odio nibh rutrum mi, id feugiat ante nisi eu risus. Vestibulum nunc orci, rhoncus a placerat in, ultricies in mi. Cras mattis varius eros, vel fringilla nisi suscipit eget.</p>
      <p>Quisque scelerisque sagittis nulla at porttitor. Mauris a justo et tellus interdum tristique. Sed id augue vitae urna euismod commodo aliquet a quam. Pellentesque arcu velit, cursus et malesuada ut, consequat et diam. Nullam erat sem, rhoncus id ullamcorper vitae, rhoncus et arcu. In ultricies ultricies nulla, ut rutrum nisi iaculis at. Donec eu magna a metus ornare faucibus. Fusce aliquet faucibus ultricies. Morbi semper, est id tincidunt gravida, sem arcu adipiscing lacus, ac bibendum nulla leo eu purus. Quisque nec diam sed risus consectetur a ccumsan quis quis nibh. Vestibulum id purus lorem.</p>
    </div>

    <div class="sender">
      <p class="sender-name">John Doe</p>
      <p class="sender-role">Co-Founder &amp; CEO</p>
    </div>

    <div class="signature" role="img" aria-label="Handwritten signature of John Doe"></div>

    <div class="contact">
      <div class="contact-row">
        <span class="contact-item phone"><span class="contact-label">T:</span>(912) 555-1234</span>
        <span class="contact-item mail"><span class="contact-label">M:</span>john@yourwebsite.com</span>
        <span class="contact-item"><span class="contact-label">W:</span>yourwebsite.com</span>
      </div>
      <div class="contact-row">
        <span class="contact-item"><span class="contact-label">A:</span>Quisque nec diam sed risus consectetur a ccumsan quis quis nibh&nbsp; quis quis nibh</span>
      </div>
    </div>
  </main>
</body>
</html>
```